Brantley Advisory Group provides support for renewable energy projects to utilities and suppliers

I need a professional looking business card that is both simple and elegant and unique. My clients are mostly large organizations not individuals. I am a consultant with my own company that is small but would like to give clients the impression I am larger. Smart grid, fiber optics, software, field hardware, distribution automation, substation automation, operations, energy storage/batteries, microgrids, customer service, strategy/roadmaps, conservation, Automated Metering Infrastruture (AMI or smart meters) are all areas of focus.

Target Market(s)

Utilities, suppliers, governmental agencies involved in energy. All types of energy especially natural gas and electrical. Especially renewable energy or green projects.

Contact Information for Business Card

Name - Mark Brantley Cell Phone - 425.318.2746 Email - mbrantley@brantleyag-example.com
Company - Brantley Advisory Group (logo) Title - Principal

Font styles to use
Serif
Sans Serif

Colors

Designer to choose colors to be used in the design.

Requirements
Must have
• Simple and professional and powerful.
• Unique/creative design.
Nice to have
• Utilize color scheme to accent logo colors. Maybe some geometric pattern on edge of card with color.
Should not have
• Busy, complicated, traditional

```html
<!DOCTYPE html>
<html lang="en">
<head>
<meta charset="utf-8">
<title>Brantley Advisory Group – Business Card</title>
<link rel="stylesheet" href="https://fonts.googleapis.com/css2?family=Varela+Round&family=Questrial&display=swap">
<style>
  :root {
    --backdrop: #c9e8de;
    --paper: #ffffff;
    --brand-violet: #2a00a6;
    --ink-black: #0b0b0b;
    --ink-dark: #1c1c1c;
    --rule: #3b1fb0;
  }
  * { box-sizing: border-box; margin: 0; padding: 0; }
  html, body {
    width: 1200px; height: 855px; overflow: hidden;
    background: var(--backdrop);
  }
  .canvas {
    position: relative; width: 1200px; height: 855px;
  }
  .card {
    position: absolute; left: 320px;
    width: 560px; height: 320px;
    border-radius: 30px; overflow: hidden;
    box-shadow: 0 10px 28px rgba(40, 90, 80, 0.18);
  }
  .card--front { top: 70px; background: var(--paper); }
  .card--back { top: 460px; background: var(--brand-violet); }

  /* wordmark */
  .wordmark {
    position: absolute; display: flex; align-items: center; gap: 14px;
    font-family: "Varela Round", sans-serif;
  }
  .wordmark__square {
    width: 34px; height: 34px; border: 3px solid currentColor; border-radius: 5px;
    flex: none;
  }
  .wordmark__text { line-height: 1.05; }
  .wordmark__lead { display: block; font-size: 34px; letter-spacing: 0.5px; }
  .wordmark__tail { display: block; font-size: 17px; letter-spacing: 0.4px; }

  .card--front .wordmark { left: 40px; top: 112px; color: var(--brand-violet); }
  .card--back .wordmark { left: 50%; top: 50%; transform: translate(-50%, -50%); color: var(--paper); gap: 20px; }
  .card--back .wordmark__square { width: 52px; height: 52px; border-width: 4px; border-radius: 7px; }
  .card--back .wordmark__lead { font-size: 50px; }
  .card--back .wordmark__tail { font-size: 25px; }

  .divider {
    position: absolute; left: 292px; top: 92px;
    width: 1.5px; height: 90px; background: var(--rule);
  }

  .contact {
    position: absolute; left: 318px; top: 86px;
    font-family: "Questrial", sans-serif; color: var(--ink-dark);
  }
  .contact__name { font-size: 21px; color: var(--brand-violet); letter-spacing: 0.3px; }
  .contact__title { font-size: 12px; margin: 2px 0 0 40px; }
  .contact__list { list-style: none; margin-top: 20px; }
  .contact__item {
    display: flex; align-items: center; gap: 9px;
    font-size: 10.5px; letter-spacing: 0.6px; margin-bottom: 7px;
  }
  .contact__icon { width: 13px; height: 13px; flex: none; }

  .footer-band { position: absolute; left: 0; bottom: 0; width: 560px; height: 50px; }
  .footer-band__label {
    position: absolute; right: 34px; bottom: 12px;
    font-family: "Questrial", sans-serif; font-size: 12.5px; letter-spacing: 0.4px;
    color: var(--paper);
  }
</style>
</head>
<body>
<main class="canvas">

  <section class="card card--front" aria-label="Business card front">
    <div class="wordmark">
      <span class="wordmark__square"></span>
      <span class="wordmark__text">
        <span class="wordmark__lead">Brantley</span>
        <span class="wordmark__tail">Advisory Group</span>
      </span>
    </div>

    <span class="divider"></span>

    <div class="contact">
      <p class="contact__name">Mark Brantley</p>
      <p class="contact__title">Principal</p>
      <ul class="contact__list">
        <li class="contact__item">
          <svg class="contact__icon" viewBox="0 0 14 14" aria-hidden="true">
            <circle cx="7" cy="7" r="7" fill="var(--brand-violet)"/>
            <path d="M4.6 3.8 l1.3 0 l0.6 1.6 l-0.8 0.6 q0.6 1.4 2 2.1 l0.6 -0.8 l1.6 0.6 l0 1.3 q-3.6 0.4 -5.3 -5.4z" fill="#fff"/>
          </svg>
          <span>425.318.2746</span>
        </li>
        <li class="contact__item">
          <svg class="contact__icon" viewBox="0 0 14 14" aria-hidden="true">
            <circle cx="7" cy="7" r="7" fill="var(--brand-violet)"/>
            <rect x="3.6" y="4.6" width="6.8" height="4.8" fill="none" stroke="#fff" stroke-width="0.9"/>
            <path d="M3.6 4.6 L7 7.3 L10.4 4.6" fill="none" stroke="#fff" stroke-width="0.9"/>
          </svg>
          <span>mbrantley@brantleyag-example.com</span>
        </li>
      </ul>
    </div>

    <svg class="footer-band" viewBox="0 0 560 50" aria-hidden="true">
      <polygon points="0,40 318,40 318,50 0,50" fill="var(--brand-violet)"/>
      <polygon points="318,40 330,14 560,14 560,50 318,50" fill="var(--ink-black)"/>
    </svg>
    <span class="footer-band__label">Brantley Advisory Group</span>
  </section>

  <section class="card card--back" aria-label="Business card back">
    <div class="wordmark">
      <span class="wordmark__square"></span>
      <span class="wordmark__text">
        <span class="wordmark__lead">Brantley</span>
        <span class="wordmark__tail">Advisory Group</span>
      </span>
    </div>
  </section>

</main>
</body>
</html>
```